Webbanner-Design für Führungskräfte-Coach
Danke für Ihr Engagement und die einwandfreie Abwicklung.
Zielgruppe
Ich coache Führungskräfte und Teams im Verkauf. Haupt-Keywort und Haupt-Thema:
Führung im Vertrieb. Das Design soll Führungskräften mit Verkaufsfunktionen gefallen.
Aufgabenstellung
Gemäss Memo (Datei: RBF-Banner-Memo).

```html
<!DOCTYPE html>
<html lang="de">
<head>
<meta charset="utf-8">
<title>Rufener Coaching &amp; Training – Webbanner</title>
<link rel="stylesheet" href="https://fonts.googleapis.com/css2?family=Arimo:wght@400;700&display=swap">
<style>
  :root {
    --sky-top: #3f7fcc;
    --sky-mid: #6ea2dc;
    --sky-bottom: #b2ceeb;
    --cloud: rgba(255, 255, 255, 0.85);
    --bar-blue: #3b73c9;
    --bar-red: #b3121c;
    --footer: #3a3a3c;
    --text-light: #ffffff;
    --photo-light: #c9d3de;
    --photo-mid: #7d8590;
    --photo-dark: #26282c;
  }
  * { margin: 0; padding: 0; box-sizing: border-box; }
  html, body { width: 1200px; height: 457px; overflow: hidden; background: #ffffff; }
  .banner {
    position: relative;
    width: 1200px;
    height: 457px;
    overflow: hidden;
    font-family: "Arimo", Arial, sans-serif;
    color: var(--text-light);
  }
  .sky {
    position: absolute;
    inset: 0;
    background: linear-gradient(180deg, var(--sky-top) 0%, var(--sky-mid) 45%, var(--sky-bottom) 100%);
  }
  .cloud-motif {
    position: absolute;
    left: 70px;
    top: 85px;
    width: 500px;
    height: 280px;
    background:
      radial-gradient(ellipse 130px 55px at 30% 72%, var(--cloud) 0%, rgba(255,255,255,0.35) 60%, transparent 100%),
      radial-gradient(ellipse 110px 70px at 62% 45%, var(--cloud) 0%, rgba(255,255,255,0.35) 60%, transparent 100%),
      radial-gradient(ellipse 60px 45px at 12% 35%, rgba(255,255,255,0.6) 0%, transparent 100%);
    filter: blur(4px);
  }
  .top-rule {
    position: absolute;
    top: 0; left: 0;
    width: 100%;
    height: 7px;
    display: flex;
  }
  .top-rule__blue { width: 616px; background: var(--bar-blue); }
  .top-rule__red { flex: 1; background: var(--bar-red); }

  .brand {
    position: absolute;
    top: 25px;
    left: 40px;
    display: flex;
    align-items: center;
    gap: 10px;
  }
  .brand__square {
    width: 66px;
    height: 66px;
    background: var(--text-light);
    opacity: 0.9;
  }
  .brand__divider {
    width: 2px;
    height: 80px;
    margin-right: 4px;
    background: var(--text-light);
  }
  .brand__name { font-size: 25px; font-weight: 700; line-height: 1.05; }
  .brand__tagline { font-size: 22.5px; font-weight: 400; line-height: 1.2; margin-top: 6px; }

  .headline {
    position: absolute;
    top: 59px;
    left: 519px;
    font-size: 27.5px;
    font-weight: 700;
    white-space: nowrap;
  }

  .portrait {
    position: absolute;
    left: 720px;
    top: 138px;
    width: 404px;
    height: 272px;
    border-radius: 140px 140px 0 0;
    background: linear-gradient(180deg, var(--photo-light) 0%, var(--photo-mid) 45%, var(--photo-dark) 100%);
  }

  .footer {
    position: absolute;
    left: 0; bottom: 0;
    width: 100%;
    height: 48px;
    background: var(--footer);
    display: flex;
    align-items: center;
    padding-left: 41px;
    font-size: 21px;
    font-weight: 700;
  }
  .contact { display: flex; align-items: center; gap: 10px; }
  .contact--mail { margin-left: 74px; }
  .contact svg { display: block; }
</style>
</head>
<body>
<div class="banner">
  <div class="sky" role="img" aria-label="Blauer Himmel"></div>
  <div class="cloud-motif" role="img" aria-label="Wolke in Form eines aufwärts zeigenden Pfeils"></div>

  <div class="top-rule">
    <div class="top-rule__blue"></div>
    <div class="top-rule__red"></div>
  </div>

  <div class="brand">
    <div class="brand__square"></div>
    <div class="brand__divider"></div>
    <div class="brand__text">
      <div class="brand__name">Rufener</div>
      <div class="brand__tagline">Coaching &amp; Training GmbH</div>
    </div>
  </div>

  <h1 class="headline">Coach für Führungskräfte und Teams im Vertrieb</h1>

  <div class="portrait" role="img" aria-label="Porträtfoto des Coachs in dunklem Sakko und hellblauem Hemd"></div>

  <div class="footer">
    <div class="contact contact--web">
      <svg width="18" height="18" viewBox="0 0 18 18" aria-hidden="true">
        <g fill="none" stroke="#ffffff" stroke-width="1.6">
          <circle cx="9" cy="9" r="7.5"/>
          <ellipse cx="9" cy="9" rx="3.3" ry="7.5"/>
          <line x1="1.5" y1="9" x2="16.5" y2="9"/>
          <line x1="3" y1="5" x2="15" y2="5"/>
          <line x1="3" y1="13" x2="15" y2="13"/>
        </g>
      </svg>
      <span>www.rbf.ch</span>
    </div>
    <div class="contact contact--mail">
      <svg width="20" height="14" viewBox="0 0 20 14" aria-hidden="true">
        <rect x="0" y="0" width="20" height="14" fill="#ffffff"/>
        <polyline points="0.8,0.8 10,8 19.2,0.8" fill="none" stroke="#3a3a3c" stroke-width="1.5"/>
      </svg>
      <span>Info@rbf.ch</span>
    </div>
  </div>
</div>
</body>
</html>
```